Plakat-Design für ein großes, geistliches Konzert für Chor, Orchester und Solisten
Zielgruppe
Wir sind eine Kantorei einer Kirchengemeinde, die in jedem Jahr ein großes Konzert für Chor, Orchester und Solisten veranstaltet. In diesem Jahr ist das Konzert in doppeltem Sinn etwas Besonderes. Zum einen weil wir das Konzert in Kooperation mit einer anderen Kantorei bestreiten und zum anderen weil die Anzahl der Mitwirkenden so groß ist, dass wir nicht der Kirche sondern das Konzert in die hiesige Stadthalle verlagern. Die Kirchenmusik präsentiert sozusagen sich außerhalb ihrer eigenen Mauern.
Eine Zielgruppe sollen diejenigen sein, die sich durch den besoneren Veranstaltungsort ansprechen lassen, also eher kirchenfremde Menschen. Das Plakat sollte auch das bestehende Stammpublikum nicht abschrecken, sondern einladen.
Es ist ein Folgeauftrag geplant, und zwar ein Programmheft/Textheft für das Konzert mit dem gleichen Design als Grundlage.
Aufgabenstellung
Das Plakat soll im DIN A3 oder A4 Hochformat erstellt werden.
Zwei weitere Logos von Förderern folgen noch.
Außer der Turm sind alle Logos von Förderern.
Der Turm ist sozusagen unser Markenzeichen und ein Wiedererkennungsmerkmal.
Das Konzert steht unter dem Motto: Von der Finsternis zum Licht.
Bezüglich der Textgröße sollte dieses Motto nicht größer sein als z.B. der Komponist und das Werk. Vielmehr soll das Motto durch ein grafisches Element eingearbeitet werden. 'Brautigorff' und 'Sternruf' sollen Eye catcher-Worte sein. Sternruf ist der Titel des Konzertes!

```html
<!DOCTYPE html>
<html lang="de">
<head>
<meta charset="utf-8">
<title>Von der Finsternis zum Licht – Konzertplakat</title>
<link rel="stylesheet" href="https://fonts.googleapis.com/css2?family=Barlow+Condensed:wght@400;500;600;700&display=swap">
<style>
  :root {
    --stage: #a7a6a9;
    --ink-dark: #0c1217;
    --teal-deep: #06364a;
    --teal: #087b97;
    --mint: #7cc7b7;
    --white: #ffffff;
    --tower-tint: rgba(60, 125, 140, 0.45);
    --footer-mint: #dff0ee;
    --logo-purple: #7a1f5e;
    --logo-dark: #1d1d1d;
  }
  * { margin: 0; padding: 0; box-sizing: border-box; }
  html, body { width: 1200px; height: 1200px; overflow: hidden; }
  body {
    background: var(--stage);
    font-family: "Barlow Condensed", "Arial Narrow", sans-serif;
    position: relative;
  }
  .poster {
    position: absolute;
    left: 217px; top: 58px;
    width: 766px; height: 1083px;
    overflow: hidden;
    background: var(--white);
    box-shadow: 0 6px 14px rgba(0,0,0,0.25);
  }
  .poster__stage {
    position: absolute; left: 0; top: 0;
    width: 766px; height: 989px;
    background:
      radial-gradient(ellipse 260px 230px at 600px 400px, rgba(160,215,222,0.85), transparent 75%),
      radial-gradient(ellipse 200px 150px at 460px 560px, rgba(0,175,210,0.9), transparent 75%),
      radial-gradient(ellipse 240px 260px at 740px 900px, rgba(110,55,30,0.95), transparent 75%),
      radial-gradient(ellipse 160px 150px at 400px 960px, rgba(80,190,205,0.8), transparent 75%),
      radial-gradient(ellipse 300px 260px at 560px 160px, rgba(30,120,140,0.8), transparent 80%),
      linear-gradient(90deg, var(--ink-dark) 0%, var(--teal-deep) 30%, var(--teal) 60%, #1b6f86 100%);
  }
  .tower-mark {
    position: absolute; left: 0; top: 60px;
    width: 262px; height: 929px;
    background: linear-gradient(180deg, rgba(60,125,140,0.15) 0%, var(--tower-tint) 35%, rgba(20,70,85,0.7) 100%);
    border-radius: 130px 130px 0 0;
  }
  .program {
    position: absolute; left: 233px; top: 52px; width: 520px;
    font-size: 26px; line-height: 30px; font-weight: 500;
    color: var(--mint); text-transform: uppercase;
  }
  .program__eye {
    display: block;
    font-size: 78px; line-height: 74px; font-weight: 700;
    color: var(--white); letter-spacing: 0.5px;
  }
  .program strong { color: var(--white); font-weight: 600; }
  .motto {
    position: absolute; left: 26px; top: 392px;
    font-size: 66px; line-height: 62px; font-weight: 500;
    text-transform: uppercase; color: var(--mint);
  }
  .motto__light { color: var(--white); }
  .credits {
    position: absolute; left: 566px; top: 556px;
    font-size: 13px; line-height: 14.3px; font-weight: 500; letter-spacing: 0.6px;
    text-transform: uppercase; color: var(--mint);
  }
  .credits p { margin-bottom: 14px; }
  .credits b { color: var(--white); font-weight: 600; }
  .date {
    position: absolute; left: 32px; top: 906px;
    font-size: 27px; line-height: 30px; font-weight: 500;
    text-transform: uppercase; color: var(--mint);
  }
  .accent { color: var(--white); font-weight: 600; }
  .footer {
    position: absolute; left: 0; top: 989px;
    width: 766px; height: 94px; background: var(--white);
  }
  .footer__tint {
    position: absolute; left: 0; top: 0; width: 341px; height: 94px;
    background: var(--footer-mint);
  }
  .sponsor {
    position: absolute; top: 36px;
    font-size: 21px; line-height: 22px; font-weight: 500;
    white-space: nowrap;
  }
  .sponsor--church { left: 243px; color: var(--logo-purple); font-size: 15px; top: 40px; }
  .sponsor--trust { left: 426px; color: var(--logo-dark); }
  .sponsor--friends { left: 627px; color: var(--logo-dark); font-weight: 600; text-transform: uppercase; font-size: 17px; top: 30px; line-height: 20px; }
</style>
</head>
<body>
  <main class="poster">
    <div class="poster__stage">
      <div class="tower-mark" role="img" aria-label="Platz für das Turm-Markenzeichen der Kantorei"></div>

      <p class="program">
        Ferdinand
        <span class="program__eye">Brautigorff</span>
        -<strong>Wendeling</strong>: Choralkantate<br>
        „Wer nur den lieben Gott lässt walten“
        <span class="program__eye">Sternruf</span>
        -Sinfonie op. 52
      </p>

      <h1 class="motto">
        Von der<br>Finsternis<br><span class="motto__light">zum Licht</span>
      </h1>

      <div class="credits">
        <p>Lena Quast und<br>Marie-Luise Fendt<br><b>Sopran</b><br>Jonas Brekke<br><b>Tenor</b></p>
        <p>Kammersinfonie Aldern<br>Kirchenkreiskantorei Birkstedt<br>Kantorei St. Ansgar, Lindholm</p>
        <p><b>Gesamtleitung</b><br>Kirchenkreiskantoren<br>Peter Wollanek (BST)<br>und Simon Haldert (LH)</p>
        <p><b>Einlass</b> 17.30 Uhr</p>
        <p><b>Eintrittspreise</b><br>25,- / 20,- / 15,- Euro<br>(Ermässigungen 50%)</p>
        <p><b>Kartenvorverkauf</b><br>Kulturverein Lindholm,<br>Mühlgasse 7, 12345 LH</p>
        <p><b>Weitere Informationen unter</b><br>www.ansgar-lindholm.de<br>www.kulturverein-lindholm.de<br>www.stadthalle-lindholm.de</p>
      </div>

      <p class="date">
        Sonntag, <span class="accent">22.09.2019</span> um <span class="accent">18.00</span><br>
        <span class="accent">Uhr</span> in der Stadthalle Lindholm
      </p>
    </div>

    <footer class="footer">
      <div class="footer__tint"></div>
      <span class="sponsor sponsor--church">Kirchenkreis Lindholm</span>
      <span class="sponsor sponsor--trust">Kreisstiftung Lindholm</span>
      <span class="sponsor sponsor--friends">Förderkreis<br>Chormusik</span>
    </footer>
  </main>
</body>
</html>
```